Residential Construction Design

I'd like a business card that really explains what we do in residential construction. A big name and number, while the other information can be smaller. Since the logo is made up of grays and a teal color, the background may have to stay white? Maybe a subtle gray.(sending 2 different color schemes of the logo for different background color options) I would like a card that just appears "tough" when you look at it.

Industry/Entity Type

Residential

Contact Information for Business Card

Name and logo which will be provided.(Rex Morton Construction, LLC) Rex Morton -Licensed Contractor, Certified Home Inspector. (555) 214-7730 Email: Rmorton_Construction@quellbox.example -Remodeling -Roofs - Siding -Drywall -Decks -Pole Barns -New Construction "Serving Southwest Michigan"

```html
<!DOCTYPE html>
<html lang="en">
<head>
<meta charset="utf-8">
<title>Rex Morton Construction, LLC — Business Card</title>
<link rel="stylesheet" href="https://fonts.googleapis.com/css2?family=Arvo:wght@700&family=Exo+2:wght@300;400&display=swap">
<style>
  :root {
    --teal: #2bbba6;
    --ink: #2b2b2b;
    --gray: #8f8f8f;
    --icon-gray: #9a9a9a;
    --rule-gray: #9aa3a3;
    --paper: #ffffff;
    --page: #ffffff;
  }
  * { box-sizing: border-box; margin: 0; padding: 0; }
  html, body {
    width: 1200px; height: 900px; overflow: hidden;
    background: var(--page);
  }
  .card {
    position: absolute; left: 264px; top: 229px;
    width: 696px; height: 377px;
    background: var(--paper);
    box-shadow: 0 2px 5px rgba(0,0,0,.45);
    overflow: hidden;
  }
  .brand {
    position: absolute; left: 62px; top: 50px;
    display: flex; align-items: center; gap: 22px;
  }
  .brand-square {
    width: 88px; height: 88px; background: var(--teal);
  }
  .brand-name {
    font-family: "Arvo", serif; font-weight: 700; color: var(--ink);
    line-height: 1.05; white-space: nowrap;
  }
  .brand-name .line-1 { display: block; font-size: 34px; }
  .brand-name .line-2 { display: block; font-size: 16px; letter-spacing: .5px; }
  .name-plate {
    position: absolute; left: 467px; top: 60px;
    width: 229px; height: 77px;
    background: var(--teal); color: var(--paper);
    text-align: center; padding-top: 11px;
  }
  .name-plate .person {
    font-family: "Arvo", serif; font-weight: 700;
    font-size: 29px; letter-spacing: 1.5px; line-height: 1;
    white-space: nowrap;
  }
  .name-plate .title {
    font-family: "Exo 2", sans-serif; font-weight: 400;
    font-size: 10px; margin-top: 9px; white-space: nowrap;
  }
  .services {
    position: absolute; left: 467px; top: 143px; width: 229px;
    text-align: center;
    font-family: "Exo 2", sans-serif; font-weight: 400;
    font-size: 9.5px; line-height: 12px; letter-spacing: .5px;
    color: var(--gray); white-space: nowrap;
  }
  .services .dot::before {
    content: ""; display: inline-block; width: 4px; height: 4px;
    background: var(--gray); margin: 0 4px 1px 4px; vertical-align: middle;
  }
  .rule {
    position: absolute; left: 0; width: 696px; height: 1px;
    background: linear-gradient(to right, var(--rule-gray) 0 467px, var(--teal) 467px);
  }
  .rule.r1 { top: 263px; }
  .rule.r2 { top: 309px; }
  .rule.r3 { top: 355px; }
  .icon {
    position: absolute; left: 429px; width: 38px; height: 38px;
    background: var(--icon-gray);
    display: flex; align-items: center; justify-content: center;
  }
  .icon.phone { top: 268px; }
  .icon.mail { top: 314px; }
  .contact {
    position: absolute; left: 467px; width: 229px; text-align: center;
    font-family: "Exo 2", sans-serif; color: var(--teal); white-space: nowrap;
  }
  .contact.phone-number {
    top: 273px; font-weight: 300; font-size: 21px; letter-spacing: 4px;
  }
  .contact.email {
    top: 326px; font-weight: 400; font-size: 9.5px; letter-spacing: .5px;
  }
</style>
</head>
<body>
  <div class="card">
    <div class="brand">
      <div class="brand-square"></div>
      <div class="brand-name">
        <span class="line-1">Rex Morton</span>
        <span class="line-2">Construction, LLC</span>
      </div>
    </div>

    <div class="name-plate">
      <div class="person">Rex Morton</div>
      <div class="title">Licensed Contractor &amp; Certified Home Inspector</div>
    </div>

    <div class="services">
      Serving on Southwest Michigan Remodeling:<br>
      <span class="dot">Roofs</span><span class="dot">Siding</span><span class="dot">Drywall</span><span class="dot">Decks</span><br>
      <span class="dot">Pole Barns</span> <span class="dot">New Construction</span>
    </div>

    <div class="rule r1"></div>
    <div class="rule r2"></div>
    <div class="rule r3"></div>

    <div class="icon phone">
      <svg width="18" height="28" viewBox="0 0 18 28" aria-hidden="true">
        <rect x="1.5" y="1.5" width="15" height="25" rx="2" fill="none" stroke="#fff" stroke-width="2"/>
        <rect x="4" y="4.5" width="10" height="17" fill="none" stroke="#fff" stroke-width="1"/>
        <circle cx="9" cy="24" r="1" fill="#fff"/>
      </svg>
    </div>
    <div class="contact phone-number">(555) 214-7730</div>

    <div class="icon mail">
      <svg width="26" height="18" viewBox="0 0 26 18" aria-hidden="true">
        <rect x="1" y="1" width="24" height="16" fill="#fff"/>
        <polyline points="1,1 13,10 25,1" fill="none" stroke="#9a9a9a" stroke-width="1.5"/>
      </svg>
    </div>
    <div class="contact email">Rmorton_Construction@quellbox.example</div>
  </div>
</body>
</html>
```